E-Waste Recycling Company Business Card

New Electronic Recycling Company based in Long Island, New York called "Baron Rustwell" We take outdated computers, components, electrical wire, circuit breakers, ink cartridges, etc. We look mostly for donated items that we recycle for our customers but will pay for large quantities from businesses. The design should reflect that we are environmentally friendly and our unique Quadra Purge process that ensures all personal data is wiped clean off hard drives. Please use our attached logo
Electrical

```html
<!DOCTYPE html>
<html lang="en">
<head>
<meta charset="utf-8">
<title>Baron Rustwell Recycling – Business Card</title>
<link rel="stylesheet" href="https://fonts.googleapis.com/css2?family=Source+Sans+3:wght@400;600;700&display=swap">
<style>
  :root {
    --page: #ecebe6;
    --green-deep: #1f8f2e;
    --green: #34a935;
    --green-bright: #7ccc2a;
    --lime: #a9d23a;
    --lime-pale: #cfe68a;
    --ink: #1d1d1d;
    --ink-soft: #3a3a3a;
    --white: #ffffff;
  }
  * { box-sizing: border-box; margin: 0; padding: 0; }
  html, body { width: 1200px; height: 902px; overflow: hidden; }
  body {
    background: var(--page);
    font-family: "Source Sans 3", "Myriad Pro", sans-serif;
    display: flex;
    flex-direction: column;
    align-items: center;
    justify-content: center;
    gap: 30px;
  }
  .card {
    position: relative;
    width: 720px;
    height: 411px;
    border-radius: 22px;
    overflow: hidden;
    box-shadow: 0 6px 18px rgba(0,0,0,.18);
  }

  /* Front */
  .card-front {
    background: radial-gradient(ellipse at 55% 40%, var(--green-bright) 0%, var(--green) 45%, var(--green-deep) 100%);
  }
  .front-brand {
    position: absolute;
    left: 0; right: 0; top: 120px;
    display: flex;
    align-items: center;
    justify-content: center;
    gap: 14px;
  }
  .brand-dot {
    width: 22px; height: 22px;
    border-radius: 50%;
    background: var(--white);
  }
  .brand-name {
    font-weight: 700;
    font-size: 46px;
    color: var(--white);
    letter-spacing: .5px;
  }
  .front-web {
    position: absolute;
    left: 0; right: 0; bottom: 58px;
    text-align: center;
    color: var(--white);
    font-size: 22px;
    letter-spacing: .5px;
  }
  .front-strip {
    position: absolute;
    left: 0; right: 0; bottom: 18px;
    height: 30px;
    background: var(--lime);
    display: flex;
    align-items: center;
    justify-content: center;
    font-size: 15px;
    color: var(--ink);
  }
  .front-strip strong { font-weight: 700; margin-right: 4px; }

  /* Back */
  .card-back { background: var(--white); }
  .back-swoosh { position: absolute; inset: 0; }
  .back-brand {
    position: absolute;
    left: 340px; top: 52px;
    display: flex;
    align-items: center;
    gap: 12px;
  }
  .card-back .brand-dot { background: var(--green); }
  .card-back .brand-name { color: var(--green); font-size: 40px; }
  .person {
    position: absolute;
    left: 44px; top: 176px;
  }
  .person-name {
    font-weight: 700;
    font-size: 26px;
    color: var(--green);
  }
  .person-title {
    font-size: 18px;
    color: var(--ink-soft);
    margin-left: 26px;
  }
  .contact {
    position: absolute;
    left: 70px; top: 250px;
    font-size: 18px;
    line-height: 25px;
    color: var(--ink);
    list-style: none;
  }
  .contact li { display: flex; align-items: center; gap: 10px; }
  .contact .icon { width: 14px; height: 14px; flex: none; }
  .contact .no-icon { width: 14px; flex: none; }
  .back-web {
    position: absolute;
    right: 36px; bottom: 22px;
    display: flex;
    align-items: center;
    gap: 8px;
    color: var(--white);
    font-size: 20px;
  }
</style>
</head>
<body>

<section class="card card-front" aria-label="Card front">
  <div class="front-brand">
    <span class="brand-dot"></span>
    <span class="brand-name">Baron Rustwell</span>
  </div>
  <p class="front-web">www.baronrustwell.com</p>
  <p class="front-strip"><strong>WE TAKE:</strong> outdated computers | components | electrical wire | circuit breakers | ink cartridges, etc</p>
</section>

<section class="card card-back" aria-label="Card back">
  <svg class="back-swoosh" viewBox="0 0 720 411" preserveAspectRatio="none" aria-hidden="true">
    <path d="M380 411 C 520 330, 640 250, 720 190 L720 411 Z" fill="var(--lime-pale)"/>
    <path d="M420 411 C 540 345, 650 270, 720 220 L720 411 Z" fill="var(--lime)"/>
    <path d="M440 411 C 560 355, 660 290, 720 250 L720 411 Z" fill="var(--green-bright)"/>
    <path d="M0 411 L0 395 C 200 390, 470 360, 720 280 L720 411 Z" fill="var(--green)"/>
    <path d="M0 411 L0 405 C 260 400, 520 385, 720 330 L720 411 Z" fill="var(--green-deep)"/>
    <path d="M300 300 C 480 260, 620 200, 720 150" stroke="var(--lime)" stroke-width="4" fill="none"/>
  </svg>

  <div class="back-brand">
    <span class="brand-dot"></span>
    <span class="brand-name">Baron Rustwell</span>
  </div>

  <div class="person">
    <p class="person-name">Your Name</p>
    <p class="person-title">Title</p>
  </div>

  <ul class="contact">
    <li><span class="no-icon"></span>48 Harbor Mill Rd</li>
    <li><span class="no-icon"></span>Suite 210 Hauppauge, NY</li>
    <li>
      <svg class="icon" viewBox="0 0 14 14" aria-hidden="true"><path d="M3 1 L5 1 L6 4 L4.5 5.2 C5.3 7 7 8.7 8.8 9.5 L10 8 L13 9 L13 11 C13 12.2 12 13 10.8 12.8 C6 12 2 8 1.2 3.2 C1 2 1.8 1 3 1 Z" fill="var(--green)"/></svg>
      (03) 5550 1234
    </li>
    <li>
      <svg class="icon" viewBox="0 0 14 14" aria-hidden="true"><rect x="3" y="1" width="8" height="12" rx="1.5" fill="var(--green)"/><rect x="4.5" y="2.5" width="5" height="6" fill="var(--white)"/><circle cx="7" cy="11" r="0.9" fill="var(--white)"/></svg>
      +44 20 7946 0321
    </li>
    <li>
      <svg class="icon" viewBox="0 0 14 14" aria-hidden="true"><rect x="1" y="3" width="12" height="8" rx="1" fill="var(--green)"/><path d="M1.5 3.5 L7 8 L12.5 3.5" stroke="var(--white)" stroke-width="1.2" fill="none"/></svg>
      info@baronrustwell.com
    </li>
  </ul>

  <p class="back-web">
    <svg width="16" height="16" viewBox="0 0 16 16" aria-hidden="true"><circle cx="8" cy="8" r="7" fill="none" stroke="var(--white)" stroke-width="1.4"/><ellipse cx="8" cy="8" rx="3" ry="7" fill="none" stroke="var(--white)" stroke-width="1.2"/><path d="M1 8 H15" stroke="var(--white)" stroke-width="1.2"/></svg>
    www.baronrustwell.com
  </p>
</section>

</body>
</html>
```